Technical audit needs a report template

As our company runs various technical audits, we also provide findings on paper, online or in Powerpoint. For this reason we need an identity pack, which includes business cards, complimentary cards, letterhead and the likes.

Who would be up to create this stationery pack for us? We hope to receive a style for these documents, that look professional and can be easily extended.
Updates

Project Deadline Extended Reason: I would like to provide the opportunity to friended designers to submit their designs too! Added Sunday, October 9, 2016

Target Market(s)

Start-ups, scale-ups and investors

Industry/Entity Type

Investment

Contact Information for Business Card

Street: Lindenhoutkade 42
Postcode: 3617KW
City: Utrecht
Country: The Netherlands
Phone: +31 302849516
Cell Phone: +31 6 58193074
email: jeroen@vexomari.example
website: https://vexomari.example

Requirements
Must have
• I don't have inspiration, should just be a slick design based on the logo provided.
Nice to have
• Logo could be on the back of the card?
Should not have
• Should not use different colours then the logo, or at least fit the colour scheme.

```html
<!DOCTYPE html>
<html lang="en">
<head>
<meta charset="utf-8">
<title>Vexomari business card</title>
<link href="https://fonts.googleapis.com/css2?family=Open+Sans:wght@400;600&display=swap" rel="stylesheet">
<style>
  :root {
    --backdrop: #3b3431;
    --card: #17181a;
    --cyan: #29a9d6;
    --cyan-light: #4cc6ee;
    --text: #e9eef1;
    --muted: #9aa3a8;
    --divider: #4a4f54;
  }
  * { margin: 0; padding: 0; box-sizing: border-box; }
  html, body { width: 1200px; height: 864px; overflow: hidden; }
  body {
    background: var(--backdrop);
    font-family: "Open Sans", Arial, sans-serif;
    position: relative;
  }
  .card {
    position: absolute;
    width: 560px;
    height: 320px;
    background: var(--card);
    border-radius: 3px;
    box-shadow: 0 18px 40px rgba(0,0,0,.45);
  }
  .card-front { left: 70px; top: 90px; }
  .card-back { left: 570px; top: 450px; }

  .front-brand {
    position: absolute;
    left: 0; right: 0; top: 108px;
    display: flex; align-items: center; justify-content: center; gap: 18px;
  }
  .brand-square {
    width: 54px; height: 54px;
    background: var(--cyan);
  }
  .brand-name {
    font-size: 46px; font-weight: 600; color: var(--cyan);
    letter-spacing: 1px;
  }
  .front-url {
    position: absolute; left: 0; right: 0; top: 214px;
    text-align: center;
    color: var(--muted); font-size: 13px; letter-spacing: 5px;
  }

  .back-brand {
    position: absolute; left: 0; top: 0; width: 260px; height: 100%;
    display: flex; flex-direction: column; align-items: center; justify-content: center; gap: 16px;
  }
  .back-brand .brand-square { width: 110px; height: 110px; background: linear-gradient(135deg, var(--cyan), var(--cyan-light)); }
  .back-brand .brand-name { font-size: 30px; }
  .back-divider {
    position: absolute; left: 262px; top: 44px; bottom: 44px;
    width: 1px; background: linear-gradient(var(--card), var(--divider), var(--card));
  }
  .contact {
    position: absolute; left: 290px; top: 44px; right: 20px;
    color: var(--text);
  }
  .contact-name { color: var(--cyan); font-size: 21px; font-weight: 600; line-height: 1.1; }
  .contact-title { font-size: 16px; margin-bottom: 14px; }
  .contact-address { font-size: 14px; line-height: 1.35; margin-bottom: 8px; }
  .contact-list { list-style: none; font-size: 14px; }
  .contact-list li { display: flex; align-items: center; gap: 10px; height: 22px; }
  .contact-list svg { width: 14px; height: 14px; flex: none; fill: var(--cyan); }
</style>
</head>
<body>
  <section class="card card-front">
    <div class="front-brand">
      <span class="brand-square"></span>
      <span class="brand-name">Vexomari</span>
    </div>
    <p class="front-url">vexomari.example</p>
  </section>

  <section class="card card-back">
    <div class="back-brand">
      <span class="brand-square"></span>
      <span class="brand-name">Vexomari</span>
    </div>
    <div class="back-divider"></div>
    <div class="contact">
      <p class="contact-name">Maren Velthuis</p>
      <p class="contact-title">President</p>
      <p class="contact-address">Lindenhoutkade 42<br>3617KW Utrecht</p>
      <ul class="contact-list">
        <li><svg viewBox="0 0 16 16"><path d="M3 1h3l1.5 4-2 1.2a9 9 0 0 0 4.3 4.3L11 8.5l4 1.5v3a2 2 0 0 1-2 2A12 12 0 0 1 1 3a2 2 0 0 1 2-2z"/></svg>+31 302849516</li>
        <li><svg viewBox="0 0 16 16"><path d="M4 0h8a1 1 0 0 1 1 1v14a1 1 0 0 1-1 1H4a1 1 0 0 1-1-1V1a1 1 0 0 1 1-1zm1 2v10h6V2zm3 11a1 1 0 1 0 0 2 1 1 0 0 0 0-2z"/></svg>+31 6 58193074</li>
        <li><svg viewBox="0 0 16 16"><path d="M4 1h8v4H4zM1 6h14v7h-3v2H4v-2H1zm4 5v3h6v-3z"/></svg>+31 302849517</li>
        <li><svg viewBox="0 0 16 16"><path d="M1 3h14v10H1zm1.5 1.2v.4L8 9l5.5-4.4v-.4z"/></svg>jeroen@vexomari.example</li>
        <li><svg viewBox="0 0 16 16"><path d="M8 0a8 8 0 1 0 0 16A8 8 0 0 0 8 0zm0 2c.9 1 1.5 2.6 1.7 5H6.3C6.5 4.6 7.1 3 8 2zM6.3 9h3.4c-.2 2.4-.8 4-1.7 5-.9-1-1.5-2.6-1.7-5z"/></svg>https://vexomari.example</li>
      </ul>
    </div>
  </section>
</body>
</html>
```